Energy Company needs a Business Card Design

We need a business card design for a new company based in Singapore called Tarn Energy. Tarn Energy is a producer of renewable energies largely for the biofuels market. Sourced entirely from sustainable resources, Tarn Energy aims to be a fully integrated oil company operating in 100% sustainable way. We would like to see designs that use the same colours as the attached file.

Industry/Entity Type

Business

```html
<!DOCTYPE html>
<html lang="en">
<head>
<meta charset="utf-8">
<title>Tarn Energy – Business Card</title>
<link rel="stylesheet" href="https://fonts.googleapis.com/css2?family=Exo+2:wght@400&display=swap">
<style>
  :root {
    --backdrop: #2e2e2f;
    --card-front: #e8e8e9;
    --card-back: #939598;
    --brand-grey: #949599;
    --brand-green: #8cc63f;
    --icon-white: #ffffff;
    --contact-text: #f4f4f5;
  }
  * { margin: 0; padding: 0; box-sizing: border-box; }
  html, body {
    width: 1200px;
    height: 1000px;
    overflow: hidden;
    background: var(--backdrop);
  }
  .canvas {
    position: relative;
    width: 1200px;
    height: 1000px;
  }
  .card {
    position: absolute;
    left: 350px;
    width: 556px;
    height: 353px;
  }
  .card--front {
    top: 141px;
    background: var(--card-front);
  }
  .card--back {
    top: 512px;
    background: var(--card-back);
  }
  .brand {
    position: absolute;
    left: 0;
    right: 0;
    top: 140px;
    display: flex;
    align-items: center;
    justify-content: center;
    gap: 14px;
  }
  .brand__name {
    font-family: "Exo 2", sans-serif;
    font-weight: 400;
    font-size: 58px;
    line-height: 1;
    color: var(--brand-grey);
    letter-spacing: 1px;
  }
  .brand__dot {
    width: 18px;
    height: 18px;
    border-radius: 50%;
    background: var(--brand-green);
  }
  .contact-list {
    position: absolute;
    left: 66px;
    top: 96px;
    list-style: none;
    display: flex;
    flex-direction: column;
    gap: 9px;
  }
  .contact-list__row {
    display: flex;
    align-items: center;
    gap: 14px;
  }
  .contact-list__icon {
    width: 34px;
    height: 34px;
    flex: none;
    background: var(--brand-green);
    display: flex;
    align-items: center;
    justify-content: center;
  }
  .contact-list__icon svg {
    width: 20px;
    height: 20px;
    fill: none;
    stroke: var(--icon-white);
    stroke-width: 2;
    stroke-linecap: round;
    stroke-linejoin: round;
  }
  .contact-list__text {
    font-family: "Exo 2", sans-serif;
    font-weight: 400;
    font-size: 15px;
    line-height: 1;
    color: var(--contact-text);
    letter-spacing: 0.3px;
    white-space: nowrap;
  }
</style>
</head>
<body>
<main class="canvas">
  <section class="card card--front" aria-label="Card front">
    <div class="brand">
      <span class="brand__name">Tarn Energy</span>
      <span class="brand__dot"></span>
    </div>
  </section>

  <section class="card card--back" aria-label="Card back">
    <ul class="contact-list">
      <li class="contact-list__row">
        <span class="contact-list__icon" aria-hidden="true">
          <svg viewBox="0 0 24 24"><path d="M3 11 12 3l9 8"/><path d="M6 10v10h12V10"/><path d="M10 20v-6h4v6"/></svg>
        </span>
        <span class="contact-list__text">12 Harbour Lane, Singapore</span>
      </li>
      <li class="contact-list__row">
        <span class="contact-list__icon" aria-hidden="true">
          <svg viewBox="0 0 24 24"><path d="M5 3h4l2 5-2.5 1.5a11 11 0 0 0 6 6L16 13l5 2v4a2 2 0 0 1-2 2A16 16 0 0 1 3 5a2 2 0 0 1 2-2z" fill="#fff"/></svg>
        </span>
        <span class="contact-list__text">+65 6123 4567</span>
      </li>
      <li class="contact-list__row">
        <span class="contact-list__icon" aria-hidden="true">
          <svg viewBox="0 0 24 24"><circle cx="12" cy="12" r="9"/><path d="M3 12h18"/><path d="M12 3a14 14 0 0 1 0 18a14 14 0 0 1 0-18z"/></svg>
        </span>
        <span class="contact-list__text">www.tarnenergy.com</span>
      </li>
      <li class="contact-list__row">
        <span class="contact-list__icon" aria-hidden="true">
          <svg viewBox="0 0 24 24"><rect x="3" y="6" width="18" height="12"/><path d="m3 6 9 7 9-7"/></svg>
        </span>
        <span class="contact-list__text">hello@tarnenergy.com</span>
      </li>
    </ul>
  </section>
</main>
</body>
</html>
```